Business cards and stationery for dental surgery products company
Dental Crestline Works, LLC
Business cards and stationery for dental surgery products company - Medical
Creative Brief
Simple
Boris Kestrow
No address.
boris.kestrow@fernmail.example
Regenerative Products Surgical Supplies
Harbor Cell Providers - Quintara Ossel Vanta Spa, USA - Disposable Surgical Devices
bkestrow bkestrow
Designers - Thanks so much for all the concepts! The world is full of amazingly creative people! I apologize for not responding recently. The holidays go me behind at my work. Then my area of the US had a winter storm that knocked out my internet service for a couple of days. So, I have been playing catch up on my work and have failed to stay on top of this project. Here are a couple of items for everyone. My website will be - www.dentalcrestlineworks.example My Facebook info is - www.socialpage.example/dentalcrestlineworks. Also, this will be my primary online vehicle. I will use it to point to my manufacturer's sites, as well as update my doctors daily. I want to remind the new comers, this is for a total stationary packet. -business cards -note / thank you cards (no need for the actual words "Thank you") -note pads -letter head -fax cover sheet -folder -simple email signature -envelopes (both regular size and also 8.5" x 11" size for literature) I hope this helps. I will let the contest run its full length of time, then post my decision sometime Monday 1/13 CST. Thanks so much! Boris
Wow! Lots of design ideas very quickly. Please remember, I need more than business cards!!
Designers - For some reason my comments did not upload correctly. What you see on the brief was from an old project that was deleted. ***Please note the following items. >>> I need a complete stationary package - business cards, thank you cards (a MUST!), note pad, letter head, folders, etc. >>> I need the business cards in white. I would like the logo on the back, with possibly a "ghosted" version of the tooth on the logo, without the name on it, enlarged and on the back of the card as well. I do not need the comments about Harbor Cell or Vanta on the cards. Nor, do I need regenerative products or disposable surgical supplies on the card. >>> I need an editable version that I can add the website, facebook, and business email address to at a later date. >>> PLEASE CONTACT ME IF YOU HAVE ANY QUESTIONS. Thanks! Boris
I'm not sure how these two got separated. I want the logo first, then use it on the business cards and stationery. Sorry for any confusion.

```html
<!DOCTYPE html>
<html lang="en">
<head>
<meta charset="utf-8">
<title>Dental Crestline Works — Business Card</title>
<link rel="stylesheet" href="https://fonts.googleapis.com/css2?family=Source+Sans+3:wght@400;600&display=swap">
<style>
  :root {
    --backdrop: #e9e6e1;
    --card: #ffffff;
    --ink: #3a3a3a;
    --brand-blue: #1f63b8;
    --deep-blue: #1a3f8f;
    --mark-grey: #9aa3ad;
    --silver-light: #eef0f2;
    --silver-dark: #a9afb6;
  }
  * { box-sizing: border-box; margin: 0; padding: 0; }
  html, body { width: 1200px; height: 818px; overflow: hidden; }
  body {
    background: var(--backdrop);
    font-family: "Source Sans 3", Arial, sans-serif;
    color: var(--ink);
    display: flex;
    align-items: center;
    justify-content: center;
    gap: 40px;
  }
  .card {
    position: relative;
    width: 540px;
    height: 310px;
    background: var(--card);
    box-shadow: 0 6px 18px rgba(0,0,0,0.18);
    overflow: hidden;
  }
  .brand {
    position: absolute;
    left: 34px;
    top: 34px;
    display: flex;
    align-items: center;
    gap: 8px;
  }
  .brand-square {
    width: 22px;
    height: 22px;
    background: var(--mark-grey);
  }
  .brand-name {
    font-size: 24px;
    font-weight: 600;
    color: var(--brand-blue);
    letter-spacing: -0.3px;
  }
  .services {
    position: absolute;
    right: 18px;
    top: 20px;
    height: 270px;
    writing-mode: vertical-rl;
    font-size: 12.5px;
    line-height: 17px;
    color: var(--ink);
  }
  .swoosh { position: absolute; inset: 0; }
  .holder-name {
    position: absolute;
    left: 300px;
    top: 112px;
    font-size: 15px;
    color: var(--ink);
  }
  .contact {
    position: absolute;
    left: 34px;
    bottom: 22px;
    list-style: none;
    font-size: 14px;
    line-height: 18px;
  }
  .contact li { display: flex; align-items: center; gap: 6px; }
  .contact svg { width: 12px; height: 12px; fill: var(--deep-blue); }
  .contact .tagline { padding-left: 0; }
</style>
</head>
<body>

  <section class="card card-back" aria-label="Card back">
    <div class="brand">
      <span class="brand-square"></span>
      <span class="brand-name">Dental Crestline Works</span>
    </div>
    <p class="services">Harbor Cell Providers - Quintara Ossel Vanta Spa<br>USA - Disposable Surgical Devices</p>
  </section>

  <section class="card card-front" aria-label="Card front">
    <svg class="swoosh" viewBox="0 0 540 310" preserveAspectRatio="none" aria-hidden="true">
      <defs>
        <linearGradient id="silver" x1="0" y1="0" x2="1" y2="1">
          <stop offset="0" stop-color="var(--silver-light)"/>
          <stop offset="1" stop-color="var(--silver-dark)"/>
        </linearGradient>
        <linearGradient id="blueBand" x1="0" y1="0" x2="0" y2="1">
          <stop offset="0" stop-color="var(--brand-blue)"/>
          <stop offset="1" stop-color="var(--deep-blue)"/>
        </linearGradient>
      </defs>
      <path d="M320 0 H540 V310 H390 C510 220 470 60 320 0 Z" fill="url(#silver)"/>
      <path d="M390 310 C510 220 470 60 320 0 L360 0 C500 70 540 210 440 310 Z" fill="url(#blueBand)"/>
    </svg>

    <div class="brand">
      <span class="brand-square"></span>
      <span class="brand-name">Dental Crestline Works</span>
    </div>

    <p class="holder-name">Boris Kestrow</p>

    <ul class="contact">
      <li><svg viewBox="0 0 12 12"><path d="M6 1 L11 6 H9.5 V11 H7 V8 H5 V11 H2.5 V6 H1 Z"/></svg>No address.</li>
      <li><svg viewBox="0 0 12 12"><path d="M2 1 h3 l1 3 -1.5 1 a6 6 0 0 0 2.5 2.5 L8 6 l3 1 v3 a1 1 0 0 1 -1 1 A9 9 0 0 1 1 2 a1 1 0 0 1 1 -1 Z"/></svg>555.014.2287</li>
      <li><svg viewBox="0 0 12 12"><path d="M1 2.5 H11 V9.5 H1 Z M1.6 3 L6 6.3 L10.4 3" stroke="#fff" stroke-width="0.8"/></svg>boris.kestrow@fernmail.example</li>
      <li class="tagline">Regenerative Products Surgical Supplies</li>
    </ul>
  </section>

</body>
</html>
```